■目的・概要 ・KPVへの出稿用バナー作成をしていただける方を募集します。 ---------------- ■注意点 ご提案頂きましたバナー案について、SNSへの投稿・Webサイトへのアップ等を行わないようにお願いします。 ※承諾頂ける方のみコンペへの参加をお願いします。 ---------------- ■依頼詳細 ・バナー内にテキストを挿入する場合は、テキストレイヤーで挿入してください。 ・テキストはおよそ1/4サイズで表示される事を考慮して制作して下さい。 ・配信時は制作したバナーがスマホの画面幅程度に縮小されて表示されます。テキストの可読性を考慮して制作お願いします ・バナー広告を見て、押したくなるようなバナー作成をお願いします。 【重要な指定】 【1】 宣伝広告したい内容 ・建売住宅(注文住宅、自由設計ではない) 【2】訴求ポイント ・地域密着 ・3000万円代から物件 ・緑区販売棟数「地域ビルダー部門」11年連続シェア№1(2008年度~2018年度㈱ミツバ総合研究所調べ) ・50年以上の販売実績 ・ミナトグループ 【3】訴求したいターゲット ・名古屋市緑区で新築住宅(建売)購入を検討している(注文住宅、自由設計ではない) ・30~40代のファミリー ・価格4000~6000万円を検討 【4】画像素材指定の無 https://kestrel-nao-ie.jp/house/ 上記サイトより転用ください。 【5】バナー制作要望 ・清潔感のあるバナーにしてほしい。 ・インパクトの強いバナーでお願いします。 ・【2】の訴求ポイントをわかりやすく伝えられるバナーにしてください。 ※このコンペは最大3件採用予定です。多数のバナーのご提案お待ちしております。 ■ 参考サイト(配信サイト) https://kestrel-nao-ie.jp/house/ ※対応方法の一部変更(9/27内容修正) ・コンペは今まで通り、1200×628 で行います。 ・採用になった作品の納品時に300×300のバナーを作成して頂き一緒に納品して頂きたいです ※300×300のバナーは採用バナーの簡易版としてつけて頂けると幸いです。 ⇒そのまま縮小というより、「メイン画像+社名(ロゴ)+一言キャッチ」くらい簡易的でOKです。 小さいバナーですので可読性を考慮して頂けると幸いです。 ■サイズと枚数 【コンペ】 ・1200 x 628 ・1枚 【納品時】 ・1200 x 628 → 1枚 ・300×300→ 1枚 ■納品ファイル ・フォトショップ形式(.psd) ■注意点・禁止事項 土日・祝日は対応することができません。 平日は9~18時までにご連絡いただければ、当日。 それ以降は翌日にご返信いたします。 ※Quilo KPVガイドラインに沿った内容である事 KPV掲載ガイドライン関連資料(http://campaignhelp.quilo.co.jp/online/doc/pdf_guideline.html) ※他で登録されているデザインや商標の転用など、他社の知的財産権を侵すこと ※他のクライアントへ既に提案した内容の転用など たくさんのウェブデザイナーの方からのご提案をお待ちしております。 |
どの案もよかったのですが、今回はこちらのバナーを特に気に入りました。
みなさんバナーの提案ありがとうございます。また依頼する際もどうぞよろしくお願いします。

```html
<!DOCTYPE html>
<html lang="ja">
<head>
<meta charset="utf-8">
<title>緑区 建売住宅 バナー</title>
<link href="https://fonts.googleapis.com/css2?family=Noto+Sans+JP:wght@500;700;900&family=Noto+Serif+JP:wght@700;900&display=swap" rel="stylesheet">
<style>
  :root {
    --night-deep: #141a24;
    --night-mid: #2b3544;
    --night-sky: #4a5a70;
    --white: #ffffff;
    --gold-light: #fff1b8;
    --gold-mid: #e3b94f;
    --gold-dark: #a9761f;
    --orange: #f08c00;
    --navy: #1b2f5e;
  }
  html, body {
    margin: 0;
    padding: 0;
    width: 1200px;
    height: 628px;
    overflow: hidden;
    background: #ffffff;
  }
  .banner {
    position: relative;
    width: 1200px;
    height: 628px;
    overflow: hidden;
    font-family: "Noto Sans JP", sans-serif;
  }
  .hero-photo {
    position: absolute;
    inset: 0;
    background:
      radial-gradient(ellipse at 85% 75%, rgba(200,167,114,0.35), transparent 45%),
      radial-gradient(ellipse at 30% 85%, rgba(200,167,114,0.2), transparent 40%),
      linear-gradient(180deg, var(--night-sky) 0%, var(--night-mid) 45%, var(--night-deep) 100%);
  }
  .headline {
    position: absolute;
    top: 18px;
    left: 0;
    width: 1200px;
    margin: 0;
    text-align: center;
    color: var(--white);
    font-weight: 900;
    font-size: 68px;
    letter-spacing: 1px;
    line-height: 1.2;
    white-space: nowrap;
    text-shadow: 0 2px 8px rgba(0,0,0,0.6);
  }
  .gold {
    font-family: "Noto Serif JP", serif;
    font-weight: 900;
    white-space: nowrap;
    background: linear-gradient(180deg, var(--gold-light) 0%, var(--gold-mid) 50%, var(--gold-dark) 100%);
    -webkit-background-clip: text;
    background-clip: text;
    color: transparent;
    filter: drop-shadow(0 2px 3px rgba(0,0,0,0.6));
  }
  .laurel {
    position: absolute;
    width: 150px;
    height: 230px;
    top: 185px;
    border-radius: 50%;
    background: radial-gradient(ellipse, rgba(227,185,79,0.55), rgba(169,118,31,0.15) 60%, transparent 72%);
  }
  .laurel-left { left: 110px; }
  .laurel-right { left: 905px; }
  .streak {
    position: absolute;
    top: 148px;
    left: 262px;
    font-size: 60px;
    line-height: 1;
  }
  .share {
    position: absolute;
    top: 235px;
    left: 318px;
    font-size: 46px;
    line-height: 1;
  }
  .rank {
    position: absolute;
    top: 118px;
    left: 565px;
    font-size: 210px;
    line-height: 1;
    letter-spacing: -4px;
  }
  .source-note {
    position: absolute;
    top: 306px;
    left: 338px;
    margin: 0;
    color: var(--white);
    font-size: 21px;
    font-weight: 500;
    white-space: nowrap;
    text-shadow: 0 1px 4px rgba(0,0,0,0.7);
  }
  .points {
    position: absolute;
    top: 462px;
    left: 8px;
    display: flex;
    gap: 12px;
    margin: 0;
    padding: 0;
    list-style: none;
  }
  .point {
    width: 150px;
    height: 150px;
    border-radius: 50%;
    background: var(--orange);
    color: var(--white);
    font-weight: 900;
    font-size: 25px;
    line-height: 1.25;
    display: flex;
    align-items: center;
    justify-content: center;
    text-align: center;
    box-shadow: 0 2px 6px rgba(0,0,0,0.35);
  }
  .cta-box {
    position: absolute;
    left: 636px;
    top: 514px;
    width: 564px;
    height: 114px;
    background: var(--white);
    display: flex;
    align-items: center;
    justify-content: space-between;
    padding: 0 18px 0 20px;
    box-sizing: border-box;
  }
  .cta-text {
    color: var(--navy);
    font-weight: 700;
    font-size: 23px;
    line-height: 1.4;
    white-space: nowrap;
  }
  .brand {
    display: flex;
    flex-direction: column;
    align-items: center;
    color: var(--navy);
    white-space: nowrap;
  }
  .brand-name {
    font-weight: 900;
    font-size: 40px;
    line-height: 1.1;
  }
  .brand-tagline {
    font-weight: 700;
    font-size: 15px;
    line-height: 1.2;
    margin-top: 6px;
  }
</style>
</head>
<body>
  <div class="banner">
    <div class="hero-photo" role="img" aria-label="夕暮れにライトアップされた緑区の建売住宅の街並み写真"></div>

    <h1 class="headline">緑区販売棟数「地域ビルダー部門」</h1>

    <div class="laurel laurel-left" role="img" aria-label="金色の月桂冠の装飾"></div>
    <div class="laurel laurel-right" role="img" aria-label="金色の月桂冠の装飾"></div>

    <div class="streak gold">11年連続</div>
    <div class="share gold">シェア</div>
    <div class="rank gold">No.1</div>
    <p class="source-note">（2008年度～2018年度㈱ミツバ総合研究所調べ）</p>

    <ul class="points">
      <li class="point">3000万円<br>台からの<br>物件多数</li>
      <li class="point">地元密着<br>50年以上の<br>販売実績</li>
      <li class="point">安心の<br>ミナト<br>グループ</li>
    </ul>

    <div class="cta-box">
      <div class="cta-text">名古屋市緑区で<br>建売住宅をお考えなら</div>
      <div class="brand">
        <span class="brand-name">ミナト不動産</span>
        <span class="brand-tagline">分譲住宅 / 土地探しサイト</span>
      </div>
    </div>
  </div>
</body>
</html>
```